Text Box for making an update on our website

We need an awesome "Text Box" so that our Users can make an amazing Post or update on our website or App.

Let's make something super duper like Pictavo, Chatterly, Quibb or Posteo text box but a bit more amazing....

I've included our current desktop and Mobile "Text Box" which needs love :)

Our Text Box by default makes a Post "Private" the User can change it to "Public"

I have included what a final "Post" looks like on our site.

Could we incorporate a bit of the "Post" design into the "Create Post" design..... maybe make the header similar.

thanks

Morgan

Target Market(s)

Health Care, Hospitals, Caregivers, Nurses

Industry/Entity Type

Health Care

Font styles to use
Other font styles liked:
• Comfortaa

Requirements
Must have
• Our main colors are

#1D44B8 - Blue
#D85097 - Pink
Nice to have
• Super clean and simple. Happy and Easy to use
Should not have
• Complicated

Too many colors

```html
<!DOCTYPE html>
<html lang="en">
<head>
<meta charset="utf-8">
<title>Create Post</title>
<link href="https://fonts.googleapis.com/css2?family=Comfortaa:wght@400;600;700&display=swap" rel="stylesheet">
<style>
  :root {
    --blue: #1D44B8;
    --header-blue: #2A50BD;
    --pink: #D85097;
    --pink-soft: #E59AC2;
    --white: #FFFFFF;
    --muted: #9AA6C4;
    --backdrop-a: #8FA57C;
    --backdrop-b: #C9D3B8;
    --backdrop-c: #6E8A5E;
  }
  * { box-sizing: border-box; margin: 0; padding: 0; }
  html, body { width: 1200px; height: 406px; overflow: hidden; }
  body { position: relative; font-family: 'Comfortaa', sans-serif; }

  .backdrop {
    position: absolute; inset: 0;
    background:
      radial-gradient(ellipse 300px 220px at 620px 60px, #E7E2D6 0%, transparent 70%),
      radial-gradient(ellipse 260px 200px at 1050px 380px, #D9D0C4 0%, transparent 70%),
      linear-gradient(120deg, var(--backdrop-c) 0%, var(--backdrop-a) 40%, var(--backdrop-b) 70%, var(--backdrop-a) 100%);
    filter: blur(2px);
  }

  .post-composer {
    position: absolute; left: 26px; top: 30px; width: 1156px; height: 352px;
    background: var(--white); border-radius: 26px; overflow: hidden;
    box-shadow: 0 6px 20px rgba(0,0,0,0.18);
  }
  .composer-header {
    position: absolute; left: 0; top: 0; width: 100%; height: 96px;
    background: var(--header-blue);
  }
  .composer-title {
    position: absolute; left: 58px; top: 28px;
    color: var(--white); font-size: 34px; font-weight: 600; letter-spacing: 0.3px;
  }
  .privacy-toggle {
    position: absolute; left: 849px; top: 24px; width: 134px; height: 50px;
    background: var(--white); border-radius: 25px;
    display: flex; align-items: center; padding-left: 14px;
    color: var(--pink); font-size: 21px; font-weight: 700;
  }
  .privacy-toggle svg { position: absolute; right: 6px; top: 5px; }
  .close-button { position: absolute; left: 1092px; top: 32px; }

  .post-input {
    position: absolute; left: 22px; top: 105px; width: 1108px; height: 74px;
    border: 2px solid var(--pink); border-radius: 3px;
  }
  .post-input .caret {
    position: absolute; left: 16px; top: 16px; width: 2px; height: 40px; background: var(--muted);
  }
  .post-input .placeholder {
    position: absolute; left: 26px; top: 18px;
    color: var(--pink-soft); font-size: 36px; font-weight: 400;
  }
  .post-input .expand { position: absolute; right: 18px; top: 18px; }

  .action-bar { position: absolute; left: 0; top: 200px; width: 100%; height: 140px; }
  .action {
    position: absolute; top: 0; width: 190px; margin-left: -95px;
    display: flex; flex-direction: column; align-items: center;
  }
  .action svg { height: 74px; }
  .action-label { margin-top: 16px; font-size: 29px; font-weight: 600; color: var(--pink); white-space: nowrap; }
  .send-button { position: absolute; left: 1024px; top: 217px; }
</style>
</head>
<body>
  <div class="backdrop" role="img" aria-label="Softly blurred outdoor photo of people in a green park"></div>

  <section class="post-composer">
    <header class="composer-header">
      <h1 class="composer-title">Create Post</h1>
      <div class="privacy-toggle">Private
        <svg width="40" height="40" viewBox="0 0 40 40">
          <circle cx="20" cy="20" r="19" fill="var(--pink)"/>
          <g stroke="#fff" stroke-width="2">
            <line x1="20" y1="4" x2="20" y2="36"/><line x1="4" y1="20" x2="36" y2="20"/>
            <line x1="9" y1="9" x2="31" y2="31"/><line x1="31" y1="9" x2="9" y2="31"/>
          </g>
          <circle cx="20" cy="20" r="5" fill="var(--pink)"/>
        </svg>
      </div>
      <svg class="close-button" width="34" height="34" viewBox="0 0 34 34">
        <path d="M4 4 L30 30 M30 4 L4 30" stroke="#fff" stroke-width="5" stroke-linecap="round"/>
      </svg>
    </header>

    <div class="post-input">
      <span class="caret"></span>
      <span class="placeholder">Share a new Post</span>
      <svg class="expand" width="38" height="38" viewBox="0 0 38 38" fill="none" stroke="var(--muted)" stroke-width="2.5" stroke-linecap="round">
        <path d="M22 4 H34 V16 M34 4 L22 16 M16 34 H4 V22 M4 34 L16 22"/>
      </svg>
    </div>

    <nav class="action-bar">
      <div class="action" style="left:148px">
        <svg viewBox="0 0 96 74" width="96">
          <rect x="18" y="4" width="74" height="52" rx="3" fill="none" stroke="var(--blue)" stroke-width="6"/>
          <rect x="4" y="16" width="76" height="54" rx="3" fill="var(--blue)"/>
          <circle cx="24" cy="32" r="6" fill="#fff"/>
          <path d="M10 64 L32 42 L44 54 L58 38 L74 64 Z" fill="#fff"/>
        </svg>
        <span class="action-label">Add Photos</span>
      </div>
      <div class="action" style="left:332px">
        <svg viewBox="0 0 60 74" width="60">
          <path d="M30 72 C14 52 4 40 4 27 A26 26 0 0 1 56 27 C56 40 46 52 30 72 Z" fill="var(--pink)"/>
          <circle cx="30" cy="27" r="15" fill="#fff"/>
          <path d="M30 36 L22 28 A4.5 4.5 0 0 1 30 22 A4.5 4.5 0 0 1 38 28 Z" fill="var(--pink)"/>
        </svg>
        <span class="action-label">Check-in</span>
      </div>
      <div class="action" style="left:520px">
        <svg viewBox="0 0 76 74" width="76">
          <path d="M6 6 H34 L72 44 L42 72 L6 36 Z" fill="var(--blue)" stroke="var(--blue)" stroke-width="4" stroke-linejoin="round"/>
          <circle cx="20" cy="20" r="5" fill="#fff"/>
          <path d="M42 58 L30 46 A6 6 0 0 1 42 37 A6 6 0 0 1 53 47 Z" fill="#fff"/>
        </svg>
        <span class="action-label">Tag Friends</span>
      </div>
      <div class="action" style="left:686px">
        <svg viewBox="0 0 74 74" width="74" fill="none" stroke="var(--pink)" stroke-width="3" stroke-linecap="round">
          <circle cx="37" cy="37" r="33"/>
          <path d="M20 30 Q25 24 30 30 M44 30 Q49 24 54 30"/>
          <path d="M20 44 Q37 60 54 44"/>
        </svg>
        <span class="action-label">Emoji</span>
      </div>
      <div class="action" style="left:832px">
        <svg viewBox="0 0 74 74" width="74" fill="none" stroke="var(--blue)" stroke-width="5" stroke-linecap="round">
          <path d="M52 26 L26 52 A9 9 0 0 1 13 39 L44 8 A13 13 0 0 1 63 27 L32 58 A17 17 0 0 1 8 34 L32 10"/>
        </svg>
        <span class="action-label">Add Files</span>
      </div>
    </nav>

    <svg class="send-button" width="90" height="90" viewBox="0 0 90 90">
      <circle cx="45" cy="45" r="45" fill="var(--blue)"/>
      <path d="M66 24 L20 44 L38 50 L44 68 Z" fill="#fff"/>
      <path d="M66 24 L38 50" stroke="var(--blue)" stroke-width="3"/>
    </svg>
  </section>
</body>
</html>
```